Brightfold

New company offering Accounting and bookkeeping for small and medium business in Cayman Islands. please see content on my website. www.brightfold.ky or www.brightfold-accountants.co.uk

Industry/Entity Type

Accounting

Requirements
Must have
• Simple, clean design
Should not have
• clutter

```html
<!DOCTYPE html>
<html lang="en">
<head>
<meta charset="utf-8">
<title>Brightfold Accountants – Flyer</title>
<link href="https://fonts.googleapis.com/css2?family=Open+Sans:wght@400;600;700;800&display=swap" rel="stylesheet">
<style>
  :root {
    --stage: #2b2d31;
    --blue: #1f78c1;
    --blue-deep: #0f4f8c;
    --blue-light: #4fa3de;
    --navy: #173a63;
    --ink: #3c4650;
    --grey: #6d7780;
    --paper: #ffffff;
    --paper-soft: #eef1f4;
    --tab: #8cc3ea;
  }
  * { box-sizing: border-box; margin: 0; padding: 0; }
  html, body { width: 900px; height: 1200px; overflow: hidden; }
  body {
    background: var(--stage);
    font-family: "Open Sans", Arial, sans-serif;
    position: relative;
  }
  .flyer {
    position: absolute;
    left: 66px;
    width: 768px;
    height: 570px;
    background: var(--paper);
    overflow: hidden;
    box-shadow: 0 10px 28px rgba(0,0,0,.45);
  }
  .flyer--front { top: 15px; }
  .flyer--back { top: 615px; background: linear-gradient(#ffffff 0%, #ffffff 22%, var(--paper-soft) 60%, #dfe4e9 100%); }

  /* brand */
  .brand {
    position: absolute;
    display: flex;
    align-items: center;
    gap: 10px;
    font-weight: 700;
    font-size: 22px;
    letter-spacing: .5px;
    white-space: nowrap;
  }
  .brand__dot { width: 30px; height: 30px; border-radius: 50%; }
  .flyer--front .brand { top: 28px; left: 50%; transform: translateX(-50%); color: var(--paper); }
  .flyer--front .brand__dot { background: var(--paper); }
  .flyer--back .brand { top: 38px; left: 50%; transform: translateX(-50%); color: var(--blue-deep); font-size: 26px; }
  .flyer--back .brand__dot { background: var(--blue); width: 36px; height: 36px; }

  /* front */
  .hero-photo {
    position: absolute; inset: 0 0 auto 0; height: 315px;
    background: linear-gradient(160deg, #dfe8ef 0%, #b9c8d6 45%, #7f97ad 100%);
  }
  .hero-top-band {
    position: absolute; top: 0; left: 0; right: 0; height: 90px;
    background: linear-gradient(180deg, rgba(15,79,140,.85), rgba(31,120,193,0));
  }
  .hero-curve { position: absolute; left: 0; top: 270px; width: 768px; height: 80px; }
  .service-box {
    position: absolute; left: 18px; width: 240px; height: 86px;
    background: linear-gradient(180deg, var(--blue-light), var(--blue-deep));
    border-radius: 6px;
    display: flex; align-items: center; gap: 12px; padding: 0 12px;
    color: var(--paper);
    box-shadow: 0 3px 8px rgba(0,0,0,.25);
  }
  .service-box--books { top: 338px; }
  .service-box--mgmt { top: 438px; }
  .service-box__icon { width: 52px; height: 52px; flex: none; }
  .service-box__title { font-weight: 700; font-size: 17px; line-height: 1.1; }
  .service-box__text { font-size: 13px; line-height: 1.2; margin-top: 3px; }
  .tagline { position: absolute; left: 292px; top: 345px; width: 440px; }
  .tagline__name { font-size: 48px; font-weight: 700; color: var(--blue); line-height: 1; }
  .tagline__line { font-size: 28px; color: var(--grey); line-height: 1.25; margin-top: 8px; }
  .tagline__line strong { color: var(--navy); font-weight: 700; }
  .front-wave { position: absolute; left: 0; bottom: 0; width: 768px; height: 70px; }

  /* back */
  .panel {
    position: absolute; top: 132px; height: 360px;
    background: linear-gradient(180deg, var(--blue-light) 0%, var(--blue) 40%, var(--blue-deep) 100%);
    border-radius: 4px;
    color: var(--paper);
    box-shadow: 0 4px 10px rgba(0,0,0,.2);
  }
  .panel--books { left: 22px; width: 312px; }
  .panel--about { left: 350px; width: 396px; }
  .panel__tab {
    position: absolute; top: -14px; left: 12px;
    background: var(--tab); color: var(--paper);
    font-size: 22px; font-weight: 700; padding: 6px 18px; border-radius: 3px;
    min-width: 200px;
    box-shadow: 0 2px 5px rgba(0,0,0,.2);
  }
  .panel__body { position: absolute; top: 48px; left: 18px; right: 16px; }
  .panel--books .panel__body { font-size: 16.5px; line-height: 1.42; }
  .panel--about .panel__body { font-size: 11.6px; line-height: 1.45; }
  .contact {
    position: absolute; right: 24px; top: 500px; text-align: right; color: var(--navy);
  }
  .contact__phone { font-size: 21px; font-weight: 700; }
  .contact__web { font-size: 15px; font-weight: 600; }
  .back-strip { position: absolute; left: 0; right: 0; bottom: 0; height: 12px; background: var(--blue); }
</style>
</head>
<body>

<section class="flyer flyer--front">
  <div class="hero-photo" role="img" aria-label="Photo of a small business team meeting around a desk with laptops"></div>
  <div class="hero-top-band"></div>
  <div class="brand"><span class="brand__dot"></span><span>Brightfold Accountants</span></div>
  <svg class="hero-curve" viewBox="0 0 768 80" preserveAspectRatio="none">
    <path d="M0 40 Q380 0 768 20 L768 80 L0 80 Z" fill="#ffffff"/>
    <path d="M0 40 Q380 0 768 20 L768 30 Q380 12 0 52 Z" fill="#1f78c1"/>
  </svg>

  <div class="service-box service-box--books">
    <svg class="service-box__icon" viewBox="0 0 52 52">
      <rect x="6" y="2" width="40" height="48" rx="4" fill="#fff"/>
      <rect x="11" y="7" width="30" height="10" fill="#1f78c1"/>
      <g fill="#1f78c1">
        <rect x="11" y="22" width="7" height="6"/><rect x="22" y="22" width="7" height="6"/><rect x="33" y="22" width="7" height="6"/>
        <rect x="11" y="31" width="7" height="6"/><rect x="22" y="31" width="7" height="6"/><rect x="33" y="31" width="7" height="6"/>
        <rect x="11" y="40" width="7" height="6"/><rect x="22" y="40" width="7" height="6"/><rect x="33" y="40" width="7" height="6"/>
      </g>
    </svg>
    <div>
      <div class="service-box__title">Bookkeeping</div>
      <div class="service-box__text">Maintaining all your accounting</div>
    </div>
  </div>

  <div class="service-box service-box--mgmt">
    <svg class="service-box__icon" viewBox="0 0 52 52">
      <rect x="2" y="2" width="48" height="48" rx="4" fill="#fff"/>
      <g fill="#1f78c1">
        <rect x="9" y="32" width="7" height="12"/><rect x="20" y="26" width="7" height="18"/>
        <rect x="31" y="20" width="7" height="24"/>
      </g>
      <path d="M8 26 L20 16 L30 20 L44 8" stroke="#0f4f8c" stroke-width="3" fill="none"/>
      <path d="M38 8 L44 8 L44 14" stroke="#0f4f8c" stroke-width="3" fill="none"/>
    </svg>
    <div>
      <div class="service-box__title">Management Accounts</div>
      <div class="service-box__text">Key business information</div>
    </div>
  </div>

  <div class="tagline">
    <div class="tagline__name">Brightfold</div>
    <div class="tagline__line"><strong>Accountants:</strong> your partner for successful growth</div>
  </div>

  <svg class="front-wave" viewBox="0 0 768 70" preserveAspectRatio="none">
    <path d="M0 60 Q400 70 768 20 L768 70 L0 70 Z" fill="#1f78c1"/>
    <path d="M0 66 Q420 74 768 38 L768 70 L0 70 Z" fill="#0f4f8c"/>
  </svg>
</section>

<section class="flyer flyer--back">
  <div class="brand"><span class="brand__dot"></span><span>Brightfold Accountants</span></div>

  <div class="panel panel--books">
    <div class="panel__tab">Bookkeeping</div>
    <p class="panel__body">Bookkeeping is one of the most critical, but often the most time consuming aspect of a business. Outsourcing your bookkeeping just makes good financial sense. You can significantly reduce your overhead costs by eliminating the need for an in-house bookkeeper, or free up the time you normally dedicate to overseeing the books.</p>
  </div>

  <div class="panel panel--about">
    <div class="panel__tab">Accountants</div>
    <p class="panel__body">Brightfold Accountants is an online, outsourced bookkeeping and accounting service provider based in the Cayman Islands. We offer all-inclusive packages at a fixed monthly fee to start-ups and small businesses who wish to run their business without the stress of bookkeeping and accounting paperwork and regulations. We take advantage of the technology available so we can drastically reduce the cost of traditional accounting services. We pass these savings on to you to offer a professional, convenient and reliable service at a fraction of the cost of full time staff or traditional accountants.</p>
  </div>

  <div class="contact">
    <div class="contact__phone">(345) 555 0182</div>
    <div class="contact__web">www.brightfold.ky</div>
  </div>

  <div class="back-strip"></div>
</section>

</body>
</html>
```